Sehr schnelle und professionelle Abwicklung. Der Designer hat mir sogar einen Fehler im Buchrücken-Text gefunden. Ich bin sehr zufrieden und kann ihn uneingeschränkt weiter empfehlen.
Zielgruppe
Wir schreiben ebooks und haben verschiedene Zielgruppen. In diesem Projekt sind es Scherheitsbewusste Eigenheimbesitzer, welche sich über die aktiven und passiven Möglichkeiten zum Einbruchschutz informieren möchten
Aufgabenstellung
Es ist ein Tatgeber zur Vermeidung von Einbrüchen. Dem Design für unser Cover sind keine Grenzen gesetzt. Es soll ansprechend sein, und Lust auf mehr Content machen.

```html
<!DOCTYPE html>
<html lang="de">
<head>
<meta charset="utf-8">
<title>Einbruchschutz – Coverentwürfe</title>
<link href="https://fonts.googleapis.com/css2?family=Open+Sans:wght@300;400;600;700&display=swap" rel="stylesheet">
<style>
  :root {
    --page: #ffffff;
    --slate: #6d6e80;
    --badge: #33363b;
    --white: #ffffff;
    --rule: #9a9a9a;
    --ink: #333333;
  }
  html, body { margin: 0; padding: 0; overflow: hidden; }
  body {
    width: 1200px; height: 2222px; position: relative;
    background: var(--page);
    font-family: 'Open Sans', Arial, sans-serif;
    color: var(--white);
  }
  .wrap-cover { position: absolute; width: 797px; height: 569px; }
  .wrap-cover--door { left: 207px; top: 140px; }
  .wrap-cover--face { left: 212px; top: 1166px; width: 794px; }
  .back-panel {
    position: absolute; left: 0; top: 0; width: 418px; height: 100%;
    background: var(--slate);
  }
  .spine-panel { position: absolute; left: 418px; top: 0; width: 0; height: 100%; }
  .front-panel { position: absolute; right: 0; top: 0; width: 379px; height: 100%; }
  .front-panel svg { display: block; }
  .wrap-cover--face .front-panel { width: 378px; }

  .back-publisher {
    position: absolute; left: 0; width: 386px; top: 24px;
    text-align: center; font-size: 9px; font-weight: 400;
  }
  .back-kicker {
    position: absolute; left: 0; width: 386px; top: 84px;
    text-align: center; font-size: 17px; font-weight: 300;
  }
  .back-title {
    position: absolute; left: 0; width: 386px; top: 106px; margin: 0;
    text-align: center; font-size: 42px; font-weight: 700; line-height: 39px;
    letter-spacing: 1px;
  }
  .back-subtitle {
    position: absolute; left: 0; width: 386px; top: 189px;
    text-align: center; font-size: 11.5px; font-weight: 400;
  }
  .back-blurb {
    position: absolute; left: 66px; width: 254px; top: 228px; margin: 0;
    text-align: center; font-size: 8.2px; line-height: 12.3px; font-weight: 400;
  }
  .back-url { position: absolute; left: 41px; top: 524px; font-size: 9px; font-weight: 600; }
  .spine-title, .spine-publisher {
    position: absolute; white-space: nowrap;
    transform: translate(-50%, -50%) rotate(-90deg);
  }
  .spine-title { left: -19px; top: 422px; font-size: 13px; font-weight: 700; }
  .spine-publisher { left: -17px; top: 77px; font-size: 8px; font-weight: 400; }

  .divider { position: absolute; height: 0; border-top: 1px dotted var(--rule); }
  .divider--first { left: 206px; top: 992px; width: 802px; }
  .divider--second { left: 211px; top: 2033px; width: 792px; }
</style>
</head>
<body>

<section class="wrap-cover wrap-cover--door">
  <div class="back-panel">
    <div class="back-publisher">Platzhalter Autor/Verlag</div>
    <div class="back-kicker">Aktiver &amp; passiver</div>
    <h2 class="back-title">EINBRUCH-<br>SCHUTZ</h2>
    <div class="back-subtitle">Der Ratgeber für sicherheitsbewußte Eigenheimbesitzer</div>
    <p class="back-blurb">Hier steht ein kurzer Text über den Inhalt des Buches. Er zeigt, wie Türen, Fenster und Keller sicherer werden, welche Technik sinnvoll ist und wie man mit einfachen Gewohnheiten Einbrechern die Arbeit schwer macht. Viele Tipps sind sofort umsetzbar und helfen, das eigene Zuhause mit wenig Aufwand spürbar besser zu schützen?</p>
    <div class="back-url">www.platzhalter-text.de</div>
  </div>
  <div class="spine-panel">
    <div class="spine-publisher">Platzhalter Autor/Verlag</div>
    <div class="spine-title">Aktiver &amp; passiver Einbruchschutz</div>
  </div>
  <div class="front-panel">
    <svg width="379" height="569" viewBox="0 0 379 569">
      <defs>
        <linearGradient id="doorTop" x1="0" x2="1" y1="0" y2="0">
          <stop offset="0" stop-color="#ececea"/>
          <stop offset="0.55" stop-color="#f4f3f0"/>
          <stop offset="0.69" stop-color="#d9d7d2"/>
          <stop offset="0.71" stop-color="#161616"/>
          <stop offset="1" stop-color="#1f1f1f"/>
        </linearGradient>
        <linearGradient id="doorBottom" x1="0" x2="1" y1="0" y2="0">
          <stop offset="0" stop-color="#e8e7e4"/>
          <stop offset="0.6" stop-color="#f2f1ee"/>
          <stop offset="0.78" stop-color="#e0dfdc"/>
          <stop offset="0.79" stop-color="#141414"/>
          <stop offset="1" stop-color="#1c1c1c"/>
        </linearGradient>
      </defs>
      <rect class="cover-photo" x="0" y="0" width="379" height="260" fill="url(#doorTop)" role="img" aria-label="Foto: weiße Tür mit goldener Klinke, dahinter ein maskierter Einbrecher"/>
      <rect class="cover-photo" x="0" y="340" width="379" height="229" fill="url(#doorBottom)" role="img" aria-label="Foto: untere Türhälfte mit behandschuhter Hand des Einbrechers"/>
      <polygon class="title-band" points="0,241 379,213 379,360 0,390" fill="var(--slate)"/>
      <g class="cover-title" fill="var(--white)" text-anchor="middle" transform="rotate(-4.25 180 300)">
        <text x="178" y="264" font-size="22" font-weight="300">Aktiver &amp; passiver</text>
        <text x="178" y="316" font-size="52" font-weight="700" textLength="282" lengthAdjust="spacingAndGlyphs">EINBRUCH-</text>
        <text x="182" y="358" font-size="52" font-weight="700" textLength="196" lengthAdjust="spacingAndGlyphs">SCHUTZ</text>
      </g>
      <g class="cover-badge">
        <circle cx="316" cy="410" r="54" fill="var(--badge)"/>
        <line x1="297" y1="382" x2="335" y2="382" stroke="var(--white)" stroke-width="1"/>
        <line x1="297" y1="439" x2="335" y2="439" stroke="var(--white)" stroke-width="1"/>
        <g fill="var(--white)" font-size="10.5" font-weight="600" text-anchor="middle">
          <text x="316" y="400">Der Ratgeber für</text>
          <text x="316" y="414">sicherheitsbewußte</text>
          <text x="316" y="428">Eigenheimbesitzer</text>
        </g>
      </g>
      <circle class="publisher-dot" cx="114" cy="538" r="10" fill="var(--slate)"/>
      <text x="134" y="542" font-size="9.5" fill="var(--ink)">Platzhalter Autor / Verlag</text>
    </svg>
  </div>
</section>

<div class="divider divider--first"></div>

<section class="wrap-cover wrap-cover--face">
  <div class="back-panel">
    <div class="back-publisher">Platzhalter Autor/Verlag</div>
    <div class="back-kicker">Aktiver &amp; passiver</div>
    <h2 class="back-title">EINBRUCH-<br>SCHUTZ</h2>
    <div class="back-subtitle">Der Ratgeber für sicherheitsbewußte Eigenheimbesitzer</div>
    <p class="back-blurb">Hier steht ein kurzer Text über den Inhalt des Buches. Er zeigt, wie Türen, Fenster und Keller sicherer werden, welche Technik sinnvoll ist und wie man mit einfachen Gewohnheiten Einbrechern die Arbeit schwer macht. Viele Tipps sind sofort umsetzbar und helfen, das eigene Zuhause mit wenig Aufwand spürbar besser zu schützen?</p>
    <div class="back-url">www.platzhalter-text.de</div>
  </div>
  <div class="spine-panel">
    <div class="spine-publisher">Platzhalter Autor/Verlag</div>
    <div class="spine-title">Aktiver &amp; passiver Einbruchschutz</div>
  </div>
  <div class="front-panel">
    <svg width="378" height="568" viewBox="0 0 378 568">
      <defs>
        <linearGradient id="faceTop" x1="0" x2="1" y1="0" y2="0">
          <stop offset="0" stop-color="#f0efec"/>
          <stop offset="0.3" stop-color="#d6d5d1"/>
          <stop offset="0.36" stop-color="#1b1b1b"/>
          <stop offset="0.7" stop-color="#3a3230"/>
          <stop offset="1" stop-color="#1a1a1a"/>
        </linearGradient>
        <linearGradient id="faceBottom" x1="0" x2="1" y1="0" y2="0">
          <stop offset="0" stop-color="#eeedea"/>
          <stop offset="0.35" stop-color="#e4dfd3"/>
          <stop offset="0.5" stop-color="#b8922a"/>
          <stop offset="0.62" stop-color="#1c1c1c"/>
          <stop offset="1" stop-color="#232323"/>
        </linearGradient>
      </defs>
      <rect class="cover-photo" x="0" y="0" width="378" height="260" fill="url(#faceTop)" role="img" aria-label="Foto: maskierter Einbrecher späht hinter einer weißen Tür hervor"/>
      <rect class="cover-photo" x="0" y="340" width="378" height="228" fill="url(#faceBottom)" role="img" aria-label="Foto: goldene Türklinke, von einer Hand im schwarzen Handschuh gegriffen"/>
      <polygon class="title-band" points="0,239 378,211 378,359 0,388" fill="var(--slate)"/>
      <g class="cover-title" fill="var(--white)" text-anchor="middle" transform="rotate(-4.25 180 300)">
        <text x="178" y="262" font-size="22" font-weight="300">Aktiver &amp; passiver</text>
        <text x="178" y="314" font-size="52" font-weight="700" textLength="282" lengthAdjust="spacingAndGlyphs">EINBRUCH-</text>
        <text x="182" y="356" font-size="52" font-weight="700" textLength="196" lengthAdjust="spacingAndGlyphs">SCHUTZ</text>
      </g>
      <g class="cover-badge">
        <circle cx="316" cy="408" r="54" fill="var(--badge)"/>
        <line x1="297" y1="380" x2="335" y2="380" stroke="var(--white)" stroke-width="1"/>
        <line x1="297" y1="437" x2="335" y2="437" stroke="var(--white)" stroke-width="1"/>
        <g fill="var(--white)" font-size="10.5" font-weight="600" text-anchor="middle">
          <text x="316" y="398">Der Ratgeber für</text>
          <text x="316" y="412">sicherheitsbewußte</text>
          <text x="316" y="426">Eigenheimbesitzer</text>
        </g>
      </g>
      <g fill="var(--white)" font-size="9.5" font-weight="600" text-anchor="middle">
        <text x="181" y="538">Platzhalter</text>
        <text x="181" y="551">Autor / Verlag</text>
      </g>
    </svg>
  </div>
</section>

<div class="divider divider--second"></div>

</body>
</html>
```